Website for Sports and Exercise Medicine Doctor with active research in stem cells therapies.

I am a sports and exercise medicine doctor with research interests in the cutting edge areas of biological therapies, most notable stem cells. None of my patients are dying of anything, and most of them come to see me to decrease their pain, so they can get back to what they want to do.

The approach i then take is to decrease their pain and support them to achieve the things they wish to achieve. Most people start at "Just make it stop hurting doc" , but I try to move them towards something more important over time.

I would like the website to be very different to other "Doctor or medical websites" in its look. No pictures of doctors in white coats and no pictures of fit old people smiling. I would potentially like the fist thing seen to be a quote:

"Less pain. Everybody wants it, but what are you going to do, once you've got it?"

(But this is only an idea, I am open to anything)

The website will need a couple of things

1. "Locations" I work
2. "Research" I am involved in
3. "Sort Me out" - Clinical information for people to access
4. "Social" - imbedded twitter and facebook
5. "Blog" - imbedded wordpress blog
6. "Bio" - the usual bio-stuff

The "Sort Me out" - pages I would like to have the functionality as seen in this site http://www.veltarion.com.au/platelet/. I intend to put disease topics into these pages (eg Achilles tehdinopathy, osteoarthritis etc etc etc). Once again I am not wedded to this but something along these lines would be good.

To give you an idea these are some sites I like
http://www.morbanquilt.com/
http://daptrine.com/
http://ovimbera.com.sg/
http://jolvaniketchup.com/
http://www.pilnorwave.com/
http://quadrisel.com/#offering
http://fennikstudio.tv/
http://norvalgate.com/
http://sablethorn.co.uk/#about

Target Market(s)

20-80 year old.
People with tendon injuries
People with osteoarthritis
People interested in stem cells
I will build the site over time to contain information on multiple sporting injuries and musculoskeletal disorders. It will also become a site for the latest on stem cell research particularly in the area of osteoarthritis.

Industry/Entity Type

Medical

Font styles to use
Sans Serif

Colors
ffffff

Requirements
Nice to have
• To give you an idea these are some sites I like
http://daptrine.com/
http://fennikstudio.tv/
http://norvalgate.com/
Should not have
• Pictures of doctors in white coats or old fit people smiling

```html
<!DOCTYPE html>
<html lang="en">
<head>
<meta charset="utf-8">
<title>Bio – Dr. Tomas Verhoek</title>
<link rel="stylesheet" href="https://fonts.googleapis.com/css2?family=Jost:ital,wght@0,300;0,400;0,500;0,600;1,300;1,600&display=swap">
<style>
  :root{
    --brand:#2490b3;
    --ink:#333333;
    --nav:#9a9a9a;
    --photo:#646464;
    --footer:#e5e5e5;
    --social:#8f8f8f;
    --band:#f1f1f1;
  }
  *{margin:0;padding:0;box-sizing:border-box}
  html,body{width:1200px;height:983px;overflow:hidden;background:#fff}
  body{position:relative;font-family:"Jost",sans-serif;color:var(--ink)}
  .abs{position:absolute}
  .logo{left:137px;top:0;width:157px;height:99px;background:var(--brand);display:flex;align-items:center;justify-content:center;color:#fff;font-weight:500;font-size:21px;letter-spacing:.5px}
  .nav{left:317px;top:38px;display:flex;gap:24px;font-weight:500;font-size:16.5px;letter-spacing:.3px;text-transform:uppercase;color:var(--nav)}
  .nav .active{color:var(--brand)}
  .title-band{left:0;top:99px;width:1200px;height:124px;background:var(--band)}
  .page-title{left:137px;top:136px;font-size:44px;font-weight:600;letter-spacing:1px;line-height:1}
  .portrait{left:138px;top:265px;width:157px;height:185px;background:var(--photo)}
  .label{left:138px;font-size:11px;font-weight:600;font-style:italic;color:var(--brand);text-transform:uppercase}
  .phone{left:137px;top:493px;font-size:24px;font-weight:400}
  .email{left:137px;top:562px;font-size:16.5px;font-weight:400}
  .intro{left:329px;top:256px;width:740px;font-weight:300;font-style:italic;letter-spacing:-.45px}
  .intro .hello{font-size:35px;line-height:42px;margin-bottom:6px}
  .intro p{font-size:22px;line-height:33.3px;margin-bottom:33px}
  .list{top:655px;width:320px}
  .list h2{font-size:15.5px;font-weight:600;color:var(--brand);text-transform:uppercase;margin-bottom:9px;letter-spacing:.1px}
  .list li{list-style:none;font-size:13px;line-height:27.7px;font-weight:400;white-space:nowrap}
  .footer{left:0;top:937px;width:1200px;height:46px;background:var(--footer)}
  .copy{left:137px;top:953px;font-size:12px;text-transform:uppercase;letter-spacing:.1px}
  .copy a{color:var(--brand);text-decoration:none}
  .social{top:945px;width:30px;height:30px;display:flex;align-items:center;justify-content:center;color:#fff;font-size:9px;font-weight:500;text-transform:uppercase;letter-spacing:.3px}
  .social.like{left:989px;background:var(--brand)}
  .social.follow{left:1031px;background:var(--social)}
</style>
</head>
<body>
  <header>
    <div class="abs logo">Dr Verhoek</div>
    <nav class="abs nav">
      <span>Home</span><span class="active">Bio</span><span>Locations</span><span>Research</span><span>Sort me out</span><span>Blog</span>
    </nav>
  </header>

  <div class="abs title-band"></div>
  <h1 class="abs page-title">BIO</h1>

  <aside>
    <div class="abs portrait" role="img" aria-label="Portrait of Dr. Tomas Verhoek"></div>
    <div class="abs label" style="top:479px">Phone:</div>
    <div class="abs phone">123 456 7890</div>
    <div class="abs label" style="top:542px">Email:</div>
    <div class="abs email">mail@drtomverhoek.com</div>
  </aside>

  <main>
    <section class="abs intro">
      <div class="hello">Hello,</div>
      <p>I’m Dr. Tomas Verhoek. I am a sports and exercise medicine doctor with research interests in the cutting edge areas of biological therapies, most notable stem cells.</p>
      <p>Lorem ipsum dolor sit amet, consectetur adipisicing elit, sed do eiusmod tempor incididunt ut labore et dolore magna aliqua. Ut enim ad minim veniam, quis nostrud exercitation ullamco laboris nisi ut aliquip ex ea commodo consequat. Sed ut perspiciatis unde omnis iste natus error sit voluptatem accusantium doloremque laudantium, totam rem aperiam, eaque ipsa quae ab illo inventore veritatis et quasi architecto beatae vitae dicta sunt explicabo.</p>
    </section>

    <section class="abs list" style="left:329px">
      <h2>Qualifications &amp; Memberships:</h2>
      <ul>
        <li>Bachelor of Science (Hons)(Uni Carrowdale)</li>
        <li>Bachelor of Medicine (Uni Port Elmore)</li>
        <li>Member of Southern College of Sports Medicine</li>
        <li>Corporate Member of Sport Health Alliance</li>
        <li>Member of the Global Cell Therapy Society</li>
      </ul>
    </section>

    <section class="abs list" style="left:664px;width:420px">
      <h2>Teams / Associations:</h2>
      <ul>
        <li>2011-Present: Harbourline FC – Team Doctor</li>
        <li>2010-2011: Northgate FC – Team Doctor</li>
        <li>2010: Global Junior Athletics Meet – Team Doctor</li>
        <li>2009: Coastline Herons Football team – Doctor</li>
        <li>2008-2009: Bayside Comets Youth league – Doctor</li>
        <li>Summit Elite Junior Basketball Program – Doctor</li>
        <li>2005-2008: Eastbrook Ranges Junior Cup Team – Doctor</li>
        <li>2008: U17 National Mens Soccer Team – Doctor (European Tour)</li>
      </ul>
    </section>
  </main>

  <footer>
    <div class="abs footer"></div>
    <div class="abs copy">Copyright © 2013 <a href="#">www.drtomverhoek.com.au</a>. All rights reserved.</div>
    <div class="abs social like">Like</div>
    <div class="abs social follow">Post</div>
  </footer>
</body>
</html>
```